Visitenkarten-Design für Goldankauf und Verkauf von Trauringen
Zielgruppe
Goldankauf und Verkauf von Trauringen
Aufgabenstellung
Edel, nicht zu bunt, das Design soll sich dem Kunden einprägen, ansprechend, gerne können auch Wasserzeichen verwendet werden.

```html
<!DOCTYPE html>
<html lang="de">
<head>
<meta charset="utf-8">
<title>Aurelia Ringhaus – Visitenkarten</title>
<link href="https://fonts.googleapis.com/css2?family=Montserrat:wght@400;500&display=swap" rel="stylesheet">
<style>
  :root {
    --page: #ffffff;
    --card-black: #0d0d0f;
    --weave-light: #6a6a6c;
    --weave-dark: #2a2a2c;
    --gold: #c9a23a;
    --text-grey: #b9b9bb;
    --title-grey: #8e8e90;
  }
  * { margin: 0; padding: 0; box-sizing: border-box; }
  html, body { width: 1200px; height: 1200px; overflow: hidden; background: var(--page); }
  body { position: relative; font-family: "Montserrat", sans-serif; }

  .card {
    position: absolute;
    left: 171px;
    width: 859px;
    background: var(--card-black);
    overflow: hidden;
  }
  .card--front { top: 50px; height: 475px; }
  .card--back { top: 652px; height: 460px; }
  .card__backdrop { position: absolute; inset: 0; width: 100%; height: 100%; }

  .brand { position: absolute; display: flex; flex-direction: column; }
  .brand__row { display: flex; align-items: center; }
  .brand__dot { border-radius: 50%; background: var(--gold); }
  .brand__name { color: var(--gold); font-weight: 500; white-space: nowrap; }
  .brand__tagline { color: var(--text-grey); font-weight: 400; letter-spacing: 0.04em; }

  .card--front .brand { left: 282px; top: 232px; }
  .card--front .brand__dot { width: 42px; height: 42px; margin-right: 16px; }
  .card--front .brand__name { font-size: 46px; }
  .card--front .brand__tagline { font-size: 19px; margin: 8px 0 0 150px; }

  .card--back .brand { left: 70px; top: 50px; }
  .card--back .brand__dot { width: 26px; height: 26px; margin-right: 10px; }
  .card--back .brand__name { font-size: 29px; }
  .card--back .brand__tagline { font-size: 12px; margin: 5px 0 0 96px; }

  .person { position: absolute; left: 526px; top: 122px; }
  .person__name { color: #c4c4c6; font-size: 33px; font-weight: 400; letter-spacing: 0.01em; }
  .person__title { color: var(--title-grey); font-size: 17px; letter-spacing: 0.28em; margin-top: 2px; }

  .contacts { position: absolute; left: 526px; top: 245px; list-style: none; }
  .contacts__item { display: flex; align-items: center; height: 37.5px; color: var(--text-grey); font-size: 14.5px; text-transform: uppercase; }
  .contacts__item--tall { height: 52px; line-height: 1.25; }
  .contacts__icon { width: 22px; height: 22px; margin-right: 26px; flex: none; fill: var(--text-grey); }
</style>
</head>
<body>

<section class="card card--front">
  <svg class="card__backdrop" viewBox="0 0 859 475" preserveAspectRatio="none" role="img" aria-label="Dunkelgrauer Bogen mit feinem Flechtmuster">
    <defs>
      <linearGradient id="weaveFront" x1="0" y1="0" x2="1" y2="1">
        <stop offset="0" stop-color="var(--weave-dark)"/>
        <stop offset="0.45" stop-color="var(--weave-light)"/>
        <stop offset="1" stop-color="var(--weave-dark)"/>
      </linearGradient>
    </defs>
    <rect width="859" height="475" fill="url(#weaveFront)"/>
    <path d="M0 30 C 40 200, 100 360, 170 475 L0 475 Z" fill="#3a3a3c" opacity="0.6"/>
    <path d="M140 475 C 240 250, 520 30, 859 0 L859 475 Z" fill="var(--card-black)"/>
  </svg>
  <div class="brand">
    <div class="brand__row"><span class="brand__dot"></span><span class="brand__name">Aurelia Ringhaus</span></div>
    <span class="brand__tagline">Goldankauf &amp; Trauringe</span>
  </div>
</section>

<section class="card card--back">
  <svg class="card__backdrop" viewBox="0 0 859 460" preserveAspectRatio="none" role="img" aria-label="Dunkelgrauer Bogen mit feinem Flechtmuster">
    <defs>
      <linearGradient id="weaveBack" x1="0" y1="0" x2="1" y2="1">
        <stop offset="0" stop-color="var(--weave-dark)"/>
        <stop offset="0.45" stop-color="var(--weave-light)"/>
        <stop offset="1" stop-color="var(--weave-dark)"/>
      </linearGradient>
    </defs>
    <rect width="859" height="460" fill="url(#weaveBack)"/>
    <path d="M0 30 C 40 200, 100 350, 170 460 L0 460 Z" fill="#3a3a3c" opacity="0.6"/>
    <path d="M140 460 C 240 240, 520 30, 859 0 L859 460 Z" fill="var(--card-black)"/>
  </svg>

  <div class="brand">
    <div class="brand__row"><span class="brand__dot"></span><span class="brand__name">Aurelia Ringhaus</span></div>
    <span class="brand__tagline">Goldankauf &amp; Trauringe</span>
  </div>

  <div class="person">
    <h1 class="person__name">MARTIN KESSLER</h1>
    <p class="person__title">CREATIVE HEAD</p>
  </div>

  <ul class="contacts">
    <li class="contacts__item">
      <svg class="contacts__icon" viewBox="0 0 24 24"><path d="M6.6 10.8a15 15 0 0 0 6.6 6.6l2.2-2.2a1 1 0 0 1 1-.25 11.4 11.4 0 0 0 3.6.57 1 1 0 0 1 1 1V20a1 1 0 0 1-1 1A17 17 0 0 1 3 4a1 1 0 0 1 1-1h3.5a1 1 0 0 1 1 1c0 1.25.2 2.45.57 3.57a1 1 0 0 1-.25 1z"/></svg>
      (555) 201-4478
    </li>
    <li class="contacts__item">
      <svg class="contacts__icon" viewBox="0 0 24 24"><path d="M12 2a10 10 0 1 0 5 18.7l-1-1.7A8 8 0 1 1 20 12v1.2a1.8 1.8 0 0 1-3.6 0V7.5h-2v.9A4.5 4.5 0 1 0 15 15.4a3.8 3.8 0 0 0 7-2.2V12A10 10 0 0 0 12 2zm0 12.5A2.5 2.5 0 1 1 14.5 12 2.5 2.5 0 0 1 12 14.5z"/></svg>
      m.kessler@ringpost.example
    </li>
    <li class="contacts__item contacts__item--tall">
      <svg class="contacts__icon" viewBox="0 0 24 24"><path d="M12 3 2 12h3v8h5v-6h4v6h5v-8h3z"/></svg>
      <span>27 Elmstone Rd,<br>Harlow, NC, 27614</span>
    </li>
    <li class="contacts__item">
      <svg class="contacts__icon" viewBox="0 0 24 24"><path d="M12 2a10 10 0 1 0 0 20 10 10 0 0 0 0-20zm6.9 9h-3a15 15 0 0 0-1.2-6 8 8 0 0 1 4.2 6zM12 4.1c.9 1.2 1.7 3.6 1.9 6.9h-3.8c.2-3.3 1-5.7 1.9-6.9zM9.3 5a15 15 0 0 0-1.2 6h-3a8 8 0 0 1 4.2-6zm-4.2 8h3a15 15 0 0 0 1.2 6 8 8 0 0 1-4.2-6zm6.9 6.9c-.9-1.2-1.7-3.6-1.9-6.9h3.8c-.2 3.3-1 5.7-1.9 6.9zm2.7-.9a15 15 0 0 0 1.2-6h3a8 8 0 0 1-4.2 6z"/></svg>
      www.aurelia-ringhaus.example
    </li>
    <li class="contacts__item">
      <svg class="contacts__icon" viewBox="0 0 24 24"><rect x="3" y="3" width="18" height="18" rx="2"/></svg>
      followaurelia
    </li>
  </ul>
</section>

</body>
</html>
```